R. T. HOLLOWAY, INC. is a US based Investment firm looking for a five-page website design.

Currently, their temporary site is located at: rtholloway.example and they would like to maintain the site design as much as possible.

R. T. HOLLOWAY, INC. sister companies are: Crestway Lodge Investments (c-lodge.example) Benwick Petroleum (benwick-petroleum.example) and RTHF (rth-foundation.example/en)

Attached is a .ZIP file with designs and assets we think will be useful for your proposal… Content for the site is attached on: rtholloway website content.docx Current temp website design is attached as: Coming Soon Website.zip .EPS Logo files attached as: rtholloway logos.zip Sample business card attached as: R T Holloway Business cards.eps Other assets, such as Fonts and background images attached as: Assets.zip

Target Market(s)

Investors

Industry/Entity Type

Investments

Number of Pages Required

5+ page

Requirements
Must have
• Contact Page with a form.

```html
<!DOCTYPE html>
<html lang="en">
<head>
<meta charset="utf-8">
<title>R. T. Holloway, Inc. — Website Presentation</title>
<link rel="stylesheet" href="https://fonts.googleapis.com/css2?family=Cinzel:wght@400;600&family=Open+Sans:wght@400;600&display=swap">
<style>
  :root {
    --navy: #2b2d3a;
    --navy-deep: #23252f;
    --gold: #b39a5e;
    --gold-light: #cdb98a;
    --cream: #f3f1ec;
    --board: #efece5;
    --white: #ffffff;
    --text: #5a5c66;
    --muted: #9a9ca4;
  }
  * { box-sizing: border-box; margin: 0; padding: 0; }
  html, body { width: 1200px; height: 3480px; overflow: hidden; }
  body { background: var(--board); font-family: "Open Sans", Arial, sans-serif; color: var(--text); }
  .board { width: 1200px; height: 3480px; position: relative; }
  .serif { font-family: "Cinzel", "Times New Roman", serif; }
  .photo { display: block; }
  .btn { display: inline-block; background: var(--gold); color: var(--white); letter-spacing: 1.2px; }
  .rule { height: 2px; background: var(--gold); }

  /* Presentation header */
  .identity { position: absolute; left: 0; top: 40px; width: 1200px; text-align: center; }
  .identity-dot { display: block; width: 46px; height: 46px; border-radius: 50%; border: 2px solid var(--gold); margin: 0 auto 14px; }
  .identity-name { font-family: "Cinzel", serif; font-size: 32px; font-weight: 400; color: var(--navy); letter-spacing: 2px; }
  .style-guide { position: absolute; top: 190px; left: 0; width: 1200px; display: flex; justify-content: center; gap: 150px; }
  .guide-block { display: flex; align-items: flex-start; gap: 14px; }
  .guide-label { font-family: "Cinzel", serif; font-weight: 600; font-size: 15px; color: var(--navy); letter-spacing: 1px; }
  .font-list { font-size: 12px; color: var(--navy); line-height: 1.5; }
  .font-list .serif { font-size: 13px; }
  .swatches { display: flex; gap: 14px; }
  .swatch { text-align: center; font-size: 8px; letter-spacing: 1px; color: var(--muted); }
  .swatch i { display: block; width: 36px; height: 36px; border-radius: 50%; margin-bottom: 5px; }
  .swatch .navy { background: var(--navy); }
  .swatch .gold { background: var(--gold); }
  .swatch .white { background: var(--white); border: 1px solid #ddd8cc; }

  .side-label { position: absolute; font-size: 13px; letter-spacing: 8px; color: var(--navy); writing-mode: vertical-rl; }
  .side-label.left { left: 78px; top: 1380px; transform: rotate(180deg); }
  .side-label.right { left: 1128px; top: 1380px; }

  /* Desktop page */
  .desk { position: absolute; left: 140px; top: 340px; width: 720px; height: 3000px; background: var(--white); box-shadow: 0 4px 20px rgba(43,45,58,0.10); font-size: 10px; line-height: 1.7; overflow: hidden; }
  .desk .brand { display: flex; align-items: center; gap: 7px; font-family: "Cinzel", serif; font-size: 11px; color: var(--navy); letter-spacing: 1px; }
  .desk .brand-dot { width: 14px; height: 14px; border-radius: 50%; background: var(--gold); }
  .desk-nav { height: 40px; display: flex; align-items: center; justify-content: space-between; padding: 0 50px; border-bottom: 1px solid #e6e3dc; }
  .desk-nav ul { display: flex; gap: 18px; list-style: none; font-size: 7.5px; letter-spacing: 0.8px; color: var(--navy); }
  .desk-nav li:first-child { color: var(--gold); }

  .desk-hero { height: 340px; background: var(--cream); position: relative; }
  .desk-hero .photo { position: absolute; right: 0; top: 0; width: 420px; height: 340px; background: linear-gradient(100deg, var(--cream) 0%, #d9d6cf 18%, #8d8e94 55%, #3a3c45 82%, #55565d 100%); }
  .desk-hero-copy { position: absolute; left: 50px; top: 100px; width: 300px; }
  .desk-hero-copy h1 { font-family: "Cinzel", serif; font-weight: 400; font-size: 22px; line-height: 1.25; color: var(--navy); letter-spacing: 0.5px; }
  .desk-hero-copy p { margin: 12px 0 18px; font-size: 10px; width: 220px; }
  .desk .btn { font-size: 8px; padding: 8px 18px; }

  .desk-band { background: var(--navy); color: var(--white); display: flex; align-items: center; justify-content: space-between; padding: 0 50px; }
  .desk-band h2 { font-family: "Cinzel", serif; font-weight: 400; font-size: 14px; letter-spacing: 1px; }
  .desk-band p { font-size: 8.5px; color: #c4c5cc; margin-top: 3px; }
  .desk-appointment { height: 100px; }
  .desk-phone { display: flex; align-items: center; gap: 7px; color: var(--gold-light); font-size: 14px; letter-spacing: 0.5px; }

  .desk-section-title { font-family: "Cinzel", serif; font-weight: 400; font-size: 18px; color: var(--navy); letter-spacing: 2px; }
  .desk-about { height: 520px; text-align: center; padding: 60px 90px 0; }
  .desk-about .rule { width: 36px; margin: 12px auto 22px; }
  .desk-emblem { display: flex; align-items: center; justify-content: center; gap: 14px; margin: 50px 0; font-family: "Cinzel", serif; font-size: 18px; color: var(--navy); letter-spacing: 2px; }
  .desk-emblem .mark { width: 90px; height: 90px; border-radius: 50%; border: 2px solid var(--gold); }

  .desk-pillars { height: 380px; display: flex; gap: 26px; padding: 10px 50px 0; }
  .desk-pillar { flex: 1; }
  .desk-pillar .photo { height: 140px; }
  .desk-pillar h3 { font-family: "Cinzel", serif; font-weight: 600; font-size: 11px; color: var(--navy); margin: 16px 0 6px; letter-spacing: 1px; }
  .desk-pillar .rule { width: 24px; margin-bottom: 8px; }
  .desk-pillar p { font-size: 9.5px; }

  .desk-leadership { height: 340px; display: flex; background: var(--cream); }
  .desk-leadership .photo { width: 320px; height: 340px; background: linear-gradient(120deg, #e9e7e2 0%, #c9c5bb 40%, #7a7b82 72%, #3e4049 100%); }
  .desk-leadership-copy { flex: 1; padding: 50px 40px 0 40px; font-size: 9.5px; }
  .desk-leadership-copy .rule { width: 36px; margin: 12px 0 16px; }
  .desk-leadership-copy p + p { margin-top: 10px; }
  .desk-leadership-copy .highlight { color: var(--gold); font-style: italic; }

  .desk-investments { height: 560px; text-align: center; padding: 56px 0 0; }
  .desk-investments .rule { width: 36px; margin: 12px auto 26px; }
  .desk-grid { display: grid; grid-template-columns: repeat(3, 200px); gap: 14px; justify-content: center; }
  .desk-card { position: relative; height: 185px; }
  .desk-card .photo { height: 185px; }
  .desk-card span { position: absolute; left: 0; bottom: 12px; background: var(--navy); color: var(--white); font-size: 7.5px; letter-spacing: 1.2px; padding: 4px 10px; }

  .desk-cta { height: 130px; }

  .desk-social { height: 360px; position: relative; background: var(--cream); }
  .desk-social .photo { position: absolute; left: 50px; top: 40px; width: 360px; height: 280px; background: linear-gradient(135deg, #6f7a86 0%, #a99d86 45%, #d6c7a8 70%, #5d6470 100%); }
  .desk-social-card { position: absolute; left: 330px; top: 80px; width: 340px; height: 200px; background: var(--white); padding: 28px 30px; box-shadow: 0 6px 20px rgba(43,45,58,0.12); font-size: 9.5px; }
  .desk-social-card .desk-section-title { font-size: 14px; }
  .desk-social-card .rule { width: 30px; margin: 10px 0 14px; }

  .desk-footer { height: 230px; background: var(--navy-deep); color: #bfc0c7; padding: 40px 50px 0; display: flex; gap: 60px; font-size: 9px; position: relative; }
  .desk-footer .brand { color: var(--white); margin-bottom: 10px; }
  .desk-footer h4 { font-family: "Cinzel", serif; font-weight: 400; font-size: 11px; color: var(--white); letter-spacing: 1px; margin-bottom: 10px; }
  .desk-footer ul { list-style: none; }
  .desk-footer-col { width: 180px; }
  .desk-copyright { position: absolute; left: 0; right: 0; bottom: 0; height: 34px; line-height: 34px; text-align: center; font-size: 8px; color: var(--muted); border-top: 1px solid #3a3c48; }

  /* Mobile page */
  .mob { position: absolute; left: 930px; top: 340px; width: 170px; height: 2600px; background: var(--white); box-shadow: 0 4px 16px rgba(43,45,58,0.10); font-size: 7.5px; line-height: 1.6; overflow: hidden; }
  .mob-nav { height: 26px; display: flex; align-items: center; justify-content: space-between; padding: 0 10px; border-bottom: 1px solid #e6e3dc; }
  .mob .brand { display: flex; align-items: center; gap: 5px; font-family: "Cinzel", serif; font-size: 7px; color: var(--navy); letter-spacing: 0.5px; }
  .mob .brand-dot { width: 9px; height: 9px; border-radius: 50%; background: var(--gold); }
  .mob-title { font-family: "Cinzel", serif; font-weight: 400; font-size: 11px; color: var(--navy); letter-spacing: 1px; }
  .mob .rule { width: 22px; margin: 7px 0 9px; }
  .mob .btn { font-size: 6px; padding: 5px 11px; }

  .mob-hero { height: 200px; background: var(--cream); position: relative; }
  .mob-hero .photo { position: absolute; right: 0; top: 0; width: 80px; height: 200px; background: linear-gradient(100deg, var(--cream) 0%, #a9a9ad 45%, #3a3c45 100%); }
  .mob-hero-copy { position: absolute; left: 10px; top: 50px; width: 150px; }
  .mob-hero-copy h1 { font-family: "Cinzel", serif; font-weight: 400; font-size: 10.5px; line-height: 1.3; color: var(--navy); }
  .mob-hero-copy p { margin: 8px 0 10px; width: 100px; font-size: 7px; }

  .mob-band { background: var(--navy); color: var(--white); padding: 22px 10px 0; }
  .mob-band h2 { font-family: "Cinzel", serif; font-weight: 400; font-size: 10px; letter-spacing: 0.5px; line-height: 1.4; }
  .mob-band p { color: #c4c5cc; font-size: 7px; margin: 6px 0 10px; }
  .mob-appointment { height: 120px; }
  .mob-phone { color: var(--gold-light); font-size: 10px; }

  .mob-about { height: 340px; padding: 24px 10px 0; }
  .mob-emblem { display: block; width: 60px; height: 60px; border-radius: 50%; border: 2px solid var(--gold); margin: 18px auto; }

  .mob-pillar { height: 170px; padding: 0 10px; }
  .mob-pillar .photo { height: 90px; }
  .mob-pillar h3 { font-family: "Cinzel", serif; font-weight: 600; font-size: 8px; color: var(--navy); margin-top: 8px; letter-spacing: 0.5px; }
  .mob-pillar .rule { margin: 4px 0 5px; }

  .mob-leadership { height: 280px; background: var(--cream); }
  .mob-leadership .photo { height: 110px; background: linear-gradient(120deg, #e9e7e2 0%, #c9c5bb 40%, #7a7b82 72%, #3e4049 100%); }
  .mob-leadership-copy { padding: 14px 10px 0; }
  .mob-leadership-copy .highlight { color: var(--gold); font-style: italic; margin-top: 6px; }

  .mob-investments { height: 510px; padding: 24px 10px 0; }
  .mob-card { position: relative; height: 70px; margin-bottom: 6px; }
  .mob-card .photo { height: 70px; }
  .mob-card span { position: absolute; left: 0; bottom: 8px; background: var(--navy); color: var(--white); font-size: 6px; letter-spacing: 1px; padding: 2px 7px; }

  .mob-cta { height: 120px; }

  .mob-social { height: 270px; background: var(--cream); padding: 14px 10px 0; }
  .mob-social .photo { height: 100px; background: linear-gradient(135deg, #6f7a86 0%, #a99d86 45%, #d6c7a8 70%, #5d6470 100%); }
  .mob-social-card { background: var(--white); padding: 12px 10px; margin-top: -10px; margin-left: 10px; position: relative; }

  .mob-footer { height: 220px; background: var(--navy-deep); color: #bfc0c7; padding: 22px 10px 0; position: relative; font-size: 7px; }
  .mob-footer .brand { color: var(--white); margin-bottom: 6px; }
  .mob-footer h4 { font-family: "Cinzel", serif; font-weight: 400; font-size: 8px; color: var(--white); margin: 12px 0 4px; }
  .mob-footer ul { list-style: none; }
  .mob-copyright { position: absolute; left: 0; right: 0; bottom: 0; height: 22px; line-height: 22px; text-align: center; font-size: 6px; color: var(--muted); border-top: 1px solid #3a3c48; }
</style>
</head>
<body>
<div class="board">

  <header class="identity">
    <span class="identity-dot"></span>
    <div class="identity-name">R. T. HOLLOWAY, INC.</div>
  </header>

  <section class="style-guide">
    <div class="guide-block">
      <span class="guide-label">FONTS:</span>
      <div class="font-list"><div class="serif">TRAJAN</div><div>Open Sans</div></div>
    </div>
    <div class="guide-block">
      <span class="guide-label">COLORS:</span>
      <div class="swatches">
        <div class="swatch"><i class="navy"></i>NAVY</div>
        <div class="swatch"><i class="gold"></i>GOLD</div>
        <div class="swatch"><i class="white"></i>WHITE</div>
      </div>
    </div>
  </section>

  <div class="side-label left">LAPTOP / DESKTOP</div>
  <div class="side-label right">RESPONSIVE SIDE</div>

  <!-- Desktop layout -->
  <main class="desk">
    <nav class="desk-nav">
      <div class="brand"><span class="brand-dot"></span>R. T. HOLLOWAY, INC.</div>
      <ul><li>HOME</li><li>ABOUT US</li><li>INVESTMENT AREAS</li><li>SOCIAL RESPONSIBILITY</li><li>CONTACT</li></ul>
    </nav>

    <header class="desk-hero">
      <div class="photo" role="img" aria-label="Business executives in suits talking in a bright boardroom"></div>
      <div class="desk-hero-copy">
        <h1>WELCOME TO<br>R. T. HOLLOWAY, INC</h1>
        <p>A trusted partner in long-term investment, growth and lasting value creation.</p>
        <span class="btn">LEARN MORE</span>
      </div>
    </header>

    <section class="desk-band desk-appointment">
      <div>
        <h2>NEED A QUICK APPOINTMENT?</h2>
        <p>Speak with one of our advisors today and schedule a meeting at your convenience.</p>
      </div>
      <div class="desk-phone">
        <svg width="14" height="14" viewBox="0 0 24 24" aria-hidden="true"><path d="M6.6 10.8a15 15 0 0 0 6.6 6.6l2.2-2.2a1 1 0 0 1 1-.25 11.4 11.4 0 0 0 3.6.57 1 1 0 0 1 1 1V20a1 1 0 0 1-1 1A17 17 0 0 1 3 4a1 1 0 0 1 1-1h3.5a1 1 0 0 1 1 1c0 1.25.2 2.45.57 3.6a1 1 0 0 1-.25 1z" fill="#cdb98a"/></svg>
        +1 555 010 2847
      </div>
    </section>

    <section class="desk-about">
      <h2 class="desk-section-title">ABOUT US</h2>
      <div class="rule"></div>
      <p>R. T. Holloway, Inc. is a privately held investment firm based in the United States. We build lasting value by partnering with strong management teams and investing across diverse sectors with patience, discipline and integrity.</p>
      <div class="desk-emblem"><span class="mark"></span>R. T. HOLLOWAY</div>
      <p>Our family of companies includes Crestway Lodge Investments, Benwick Petroleum and the RTHF foundation, each committed to responsible growth.</p>
    </section>

    <section class="desk-pillars">
      <article class="desk-pillar">
        <div class="photo" role="img" aria-label="Business team reviewing documents at a desk" style="background:linear-gradient(135deg,#cfd3d8,#7d838c);"></div>
        <h3>MISSION</h3><div class="rule"></div>
        <p>To deliver sustainable returns by investing with care in businesses that create real value for communities.</p>
      </article>
      <article class="desk-pillar">
        <div class="photo" role="img" aria-label="Hands pointing at charts on a laptop" style="background:linear-gradient(135deg,#e2ddd2,#8f8a80);"></div>
        <h3>VISION</h3><div class="rule"></div>
        <p>To be the most respected long-term partner for investors seeking steady growth across many industries.</p>
      </article>
      <article class="desk-pillar">
        <div class="photo" role="img" aria-label="Two business partners shaking hands" style="background:linear-gradient(135deg,#c8ccd1,#50545e);"></div>
        <h3>VALUES</h3><div class="rule"></div>
        <p>Integrity, discipline and transparency guide every decision we make for our clients and our partners.</p>
      </article>
    </section>

    <section class="desk-leadership">
      <div class="photo" role="img" aria-label="Executive presenting a growth chart to colleagues"></div>
      <div class="desk-leadership-copy">
        <h2 class="desk-section-title">LEADERSHIP</h2>
        <div class="rule"></div>
        <p>Our leadership team brings decades of experience in finance, energy and hospitality. Together they set a clear direction for the firm and guide each investment from first review to long-term ownership.</p>
        <p class="highlight">We believe strong leadership is the foundation of every lasting investment.</p>
        <p>Working closely with our sister companies, they share knowledge, manage risk and keep our focus on the needs of our investors.</p>
      </div>
    </section>

    <section class="desk-investments">
      <h2 class="desk-section-title">INVESTMENT AREAS</h2>
      <div class="rule"></div>
      <div class="desk-grid">
        <div class="desk-card"><div class="photo" role="img" aria-label="Hotel lobby interior" style="background:linear-gradient(135deg,#d8c9a6,#7c6a4c);"></div><span>HOSPITALITY</span></div>
        <div class="desk-card"><div class="photo" role="img" aria-label="Modern office building" style="background:linear-gradient(135deg,#c9d0d8,#5d6672);"></div><span>REAL ESTATE</span></div>
        <div class="desk-card"><div class="photo" role="img" aria-label="Oil refinery at dusk" style="background:linear-gradient(135deg,#b9bcc2,#454952);"></div><span>ENERGY</span></div>
        <div class="desk-card"><div class="photo" role="img" aria-label="Calculator and financial papers" style="background:linear-gradient(135deg,#e4e1da,#9a968c);"></div><span>FINANCE</span></div>
        <div class="desk-card"><div class="photo" role="img" aria-label="Laptop on a work desk" style="background:linear-gradient(135deg,#d0d3d6,#6e737a);"></div><span>TECHNOLOGY</span></div>
        <div class="desk-card"><div class="photo" role="img" aria-label="Green farm fields" style="background:linear-gradient(135deg,#c7c9a4,#6f7a4e);"></div><span>AGRICULTURE</span></div>
      </div>
    </section>

    <section class="desk-band desk-cta">
      <div>
        <h2>LOREM IPSUM DOLOR AMET?</h2>
        <p>Reach our team to discuss new opportunities and partnerships with us.</p>
      </div>
      <span class="btn">CONTACT US</span>
    </section>

    <section class="desk-social">
      <div class="photo" role="img" aria-label="Group of smiling children outdoors"></div>
      <div class="desk-social-card">
        <h2 class="desk-section-title">SOCIAL RESPONSIBILITY</h2>
        <div class="rule"></div>
        <p>Through the RTHF foundation we support education, health and community projects. We believe investing in people is as important as investing in business, and we give back wherever we work.</p>
      </div>
    </section>

    <footer class="desk-footer">
      <div class="desk-footer-col">
        <div class="brand"><span class="brand-dot"></span>R. T. HOLLOWAY, INC.</div>
        <p>A US based investment firm building lasting value for investors and communities.</p>
      </div>
      <div class="desk-footer-col">
        <h4>QUICK LINKS</h4>
        <ul><li>Home</li><li>About Us</li><li>Investment Areas</li><li>Social Responsibility</li><li>Contact</li></ul>
      </div>
      <div class="desk-footer-col">
        <h4>CONTACT</h4>
        <ul><li>400 Harbor Lane, Suite 12, Springfield, US</li><li>+1 555 010 2847</li><li>info@rtholloway.example</li></ul>
      </div>
      <div class="desk-copyright">© R. T. Holloway, Inc. All rights reserved.</div>
    </footer>
  </main>

  <!-- Mobile layout -->
  <aside class="mob">
    <nav class="mob-nav">
      <div class="brand"><span class="brand-dot"></span>R. T. HOLLOWAY</div>
      <svg width="12" height="9" viewBox="0 0 12 9" aria-hidden="true"><rect width="12" height="1.4" fill="#2b2d3a"/><rect y="3.8" width="12" height="1.4" fill="#2b2d3a"/><rect y="7.6" width="12" height="1.4" fill="#2b2d3a"/></svg>
    </nav>

    <header class="mob-hero">
      <div class="photo" role="img" aria-label="Business executives in suits talking in a boardroom"></div>
      <div class="mob-hero-copy">
        <h1>WELCOME TO<br>R. T. HOLLOWAY, INC</h1>
        <p>A trusted partner in long-term investment and growth.</p>
        <span class="btn">LEARN MORE</span>
      </div>
    </header>

    <section class="mob-band mob-appointment">
      <h2>NEED A QUICK<br>APPOINTMENT?</h2>
      <p>Speak with one of our advisors today.</p>
      <div class="mob-phone">+1 555 010 2847</div>
    </section>

    <section class="mob-about">
      <h2 class="mob-title">ABOUT US</h2>
      <div class="rule"></div>
      <p>R. T. Holloway, Inc. is a privately held investment firm based in the United States, building lasting value with patience and integrity.</p>
      <span class="mob-emblem"></span>
      <p>Our family includes Crestway Lodge Investments, Benwick Petroleum and the RTHF foundation.</p>
    </section>

    <article class="mob-pillar">
      <div class="photo" role="img" aria-label="Business team reviewing documents" style="background:linear-gradient(135deg,#cfd3d8,#7d838c);"></div>
      <h3>MISSION</h3><div class="rule"></div>
      <p>To deliver sustainable returns that create real value.</p>
    </article>
    <article class="mob-pillar">
      <div class="photo" role="img" aria-label="Hands pointing at charts on a laptop" style="background:linear-gradient(135deg,#e2ddd2,#8f8a80);"></div>
      <h3>VISION</h3><div class="rule"></div>
      <p>To be the most respected long-term investment partner.</p>
    </article>
    <article class="mob-pillar">
      <div class="photo" role="img" aria-label="Two business partners shaking hands" style="background:linear-gradient(135deg,#c8ccd1,#50545e);"></div>
      <h3>VALUES</h3><div class="rule"></div>
      <p>Integrity, discipline and transparency in every decision.</p>
    </article>

    <section class="mob-leadership">
      <div class="photo" role="img" aria-label="Executive presenting a growth chart"></div>
      <div class="mob-leadership-copy">
        <h2 class="mob-title">LEADERSHIP</h2>
        <div class="rule"></div>
        <p>Our leaders bring decades of experience in finance, energy and hospitality, guiding each investment from first review to ownership.</p>
        <p class="highlight">Strong leadership is the foundation of every investment.</p>
      </div>
    </section>

    <section class="mob-investments">
      <h2 class="mob-title">INVESTMENT AREAS</h2>
      <div class="rule"></div>
      <div class="mob-card"><div class="photo" role="img" aria-label="Hotel lobby interior" style="background:linear-gradient(135deg,#d8c9a6,#7c6a4c);"></div><span>HOSPITALITY</span></div>
      <div class="mob-card"><div class="photo" role="img" aria-label="Modern office building" style="background:linear-gradient(135deg,#c9d0d8,#5d6672);"></div><span>REAL ESTATE</span></div>
      <div class="mob-card"><div class="photo" role="img" aria-label="Oil refinery at dusk" style="background:linear-gradient(135deg,#b9bcc2,#454952);"></div><span>ENERGY</span></div>
      <div class="mob-card"><div class="photo" role="img" aria-label="Calculator and financial papers" style="background:linear-gradient(135deg,#e4e1da,#9a968c);"></div><span>FINANCE</span></div>
      <div class="mob-card"><div class="photo" role="img" aria-label="Laptop on a work desk" style="background:linear-gradient(135deg,#d0d3d6,#6e737a);"></div><span>TECHNOLOGY</span></div>
      <div class="mob-card"><div class="photo" role="img" aria-label="Green farm fields" style="background:linear-gradient(135deg,#c7c9a4,#6f7a4e);"></div><span>AGRICULTURE</span></div>
    </section>

    <section class="mob-band mob-cta">
      <h2>LOREM IPSUM<br>DOLOR AMET?</h2>
      <p>Reach our team to discuss new opportunities.</p>
      <span class="btn">CONTACT US</span>
    </section>

    <section class="mob-social">
      <div class="photo" role="img" aria-label="Group of smiling children outdoors"></div>
      <div class="mob-social-card">
        <h2 class="mob-title">SOCIAL<br>RESPONSIBILITY</h2>
        <div class="rule"></div>
        <p>Through the RTHF foundation we support education, health and community projects wherever we work.</p>
      </div>
    </section>

    <footer class="mob-footer">
      <div class="brand"><span class="brand-dot"></span>R. T. HOLLOWAY, INC.</div>
      <p>A US based investment firm building lasting value.</p>
      <h4>QUICK LINKS</h4>
      <ul><li>Home · About Us · Investment Areas</li><li>Social Responsibility · Contact</li></ul>
      <h4>CONTACT</h4>
      <ul><li>+1 555 010 2847</li><li>info@rtholloway.example</li></ul>
      <div class="mob-copyright">© R. T. Holloway, Inc.</div>
    </footer>
  </aside>

</div>
</body>
</html>
```